TRESSLY FACEBOOK DESIGN

I need new design for facebook https://www.facebook.com/tresslyitalia.
Our Businnes is Hair care , hair replacement , hair transplant . hair regrowth . i NEED MEDICAL AND PROFESSIONAL DESIGN. I NEED ALSO RESPONSIVE DESIGN

Target Market(s)

Consumers

Industry/Entity Type

MEDICAL AND COSMETICS

Colors
0054AA
0677BA
7BADD7
CADEEF
E8F1F8

Requirements
Must have
• MEDICAL
Nice to have
• RESPONSIVE DESIGN

```html
<!DOCTYPE html>
<html lang="it">
<head>
<meta charset="utf-8">
<title>Tressly – Facebook cover</title>
<link rel="stylesheet" href="https://fonts.googleapis.com/css2?family=Quicksand:wght@500;700&family=Roboto:wght@700;900&display=swap">
<style>
  :root {
    --blue-deep: #0054AA;
    --blue-mid: #0677BA;
    --blue-sky: #29A8E0;
    --blue-soft: #7BADD7;
    --blue-pale: #CADEEF;
    --blue-mist: #E8F1F8;
    --white: #ffffff;
  }
  html, body {
    margin: 0;
    padding: 0;
    width: 1200px;
    height: 900px;
    overflow: hidden;
    background: var(--blue-mist);
  }
  .stage {
    position: relative;
    width: 1200px;
    height: 900px;
  }
  .cover {
    position: absolute;
    left: 40px;
    top: 235px;
    width: 888px;
    height: 340px;
    transform: scale(1.2613);
    transform-origin: top left;
    background: var(--white);
    overflow: hidden;
    box-shadow: 0 2px 10px rgba(0, 40, 90, 0.15);
  }
  .cover__shapes {
    position: absolute;
    inset: 0;
    width: 888px;
    height: 340px;
  }
  .brand {
    position: absolute;
    left: 540px;
    top: 52px;
    display: flex;
    align-items: center;
    gap: 12px;
  }
  .brand__mark {
    width: 52px;
    height: 52px;
    background: var(--blue-sky);
    border-radius: 6px;
  }
  .brand__name {
    font-family: "Quicksand", sans-serif;
    font-weight: 700;
    font-size: 64px;
    line-height: 1;
    color: var(--blue-deep);
    letter-spacing: 0.5px;
  }
  .brand__tagline {
    position: absolute;
    left: 540px;
    top: 130px;
    width: 330px;
    margin: 0;
    text-align: center;
    font-family: "Quicksand", sans-serif;
    font-weight: 500;
    font-size: 16.5px;
    line-height: 20px;
    color: var(--blue-mid);
    letter-spacing: 0.4px;
    white-space: nowrap;
  }
  .contact {
    position: absolute;
    left: 500px;
    top: 212px;
    width: 368px;
    color: var(--white);
    font-family: "Roboto", sans-serif;
  }
  .contact__phone {
    margin: 0 0 10px;
    text-align: right;
    font-weight: 700;
    font-size: 47px;
    line-height: 1;
  }
  .services {
    list-style: none;
    margin: 0;
    padding: 0;
    font-weight: 700;
    font-size: 14.5px;
    line-height: 18px;
    letter-spacing: 0.3px;
  }
  .services__row {
    display: flex;
    justify-content: flex-end;
    gap: 10px;
    margin-bottom: 8px;
  }
  .services__row--first { justify-content: center; padding-left: 80px; }
  .services__item::before {
    content: "";
    display: inline-block;
    width: 8px;
    height: 8px;
    border-radius: 50%;
    background: var(--white);
    margin-right: 6px;
    vertical-align: 2px;
  }
</style>
</head>
<body>
<main class="stage">
  <section class="cover" aria-label="Tressly Facebook cover">
    <svg class="cover__shapes" viewBox="0 0 888 340" xmlns="http://www.w3.org/2000/svg">
      <defs>
        <linearGradient id="treatment-tones" x1="0" y1="0" x2="1" y2="1">
          <stop offset="0" stop-color="#eeeeee"/>
          <stop offset="1" stop-color="#b9b9b9"/>
        </linearGradient>
        <linearGradient id="man-tones" x1="0" y1="0" x2="1" y2="1">
          <stop offset="0" stop-color="#d9d7d5"/>
          <stop offset="1" stop-color="#b88d73"/>
        </linearGradient>
        <linearGradient id="woman-tones" x1="0" y1="0" x2="1" y2="1">
          <stop offset="0" stop-color="#8a4a2c"/>
          <stop offset="0.55" stop-color="#d8b9a6"/>
          <stop offset="1" stop-color="#f1ece8"/>
        </linearGradient>
      </defs>

      <!-- left frame band -->
      <polygon points="0,0 262,0 196,148 262,308 256,340 0,340" fill="var(--blue-sky)"/>
      <!-- hexagon frame -->
      <polygon points="262,0 452,0 535,148 459,308 262,308 196,148" fill="var(--blue-sky)"/>

      <!-- photo areas -->
      <polygon role="img" aria-label="Photo of a woman receiving a scalp treatment"
               points="0,0 238,0 188,142 0,142" fill="url(#treatment-tones)"/>
      <polygon role="img" aria-label="Photo of a smiling man holding his hair"
               points="0,158 186,158 250,340 0,340" fill="url(#man-tones)"/>
      <polygon role="img" aria-label="Photo of a smiling woman with long flowing hair"
               points="270,6 446,6 526,148 453,301 268,301 205,148" fill="url(#woman-tones)"/>

      <!-- contact panel -->
      <path d="M888 201 H566 Q550 201 543 215 L486 314 Q482 318 474 318 H300 Q272 318 260 340"
            fill="none" stroke="var(--blue-sky)" stroke-width="4"/>
      <path d="M888 208 H569 Q556 208 550 220 L494 320 Q489 325 480 325 H306 Q286 325 276 340 H888 Z"
            fill="var(--blue-deep)"/>

      <!-- tagline swoosh -->
      <path d="M540 170 Q700 192 866 160 Q700 182 540 170 Z" fill="var(--blue-sky)"/>
    </svg>

    <div class="brand">
      <span class="brand__mark" aria-hidden="true"></span>
      <span class="brand__name">Tressly</span>
    </div>
    <p class="brand__tagline">CURA E REINTEGRAZIONE DEI CAPELLI</p>

    <div class="contact">
      <p class="contact__phone">000-555-0199</p>
      <ul class="services">
        <li class="services__row services__row--first"><span class="services__item">HAIR CARE</span></li>
        <li class="services__row"><span class="services__item">HAIR REPLACEMENT</span><span class="services__item">HAIR TRANSPLANT</span></li>
      </ul>
    </div>
  </section>
</main>
</body>
</html>
```